2 guided dives on the North of Bonaire

2 guided shore dives on the North of Bonaire including authentic local lunch and drinks.
We offer an adventure for experienced divers to discover the dive sites on the north of the island.
Showing you the beauty of the reefs and tasting authentic local cuisine like goat or iguana combined with a stunning view of the surroundings.

Target Market(s)

Divers / tourism

Industry/Entity Type

Tourism / Diving

Font styles to use
Sans Serif

Colors
0054AA
0677BA
7BADD7
CADEEF
E8F1F8
0094D4
00A9DD
6FCCEA
C7EBF8
E9F6FB
F0912C
F2A743
F7CA91
FBE8D2
FDF5EE
EE7325
F08F49
F5BC92
FAE3D3
FDF4ED

Requirements
Must have
• Some of the pictures I uploaded and the food picture / bottom like in the pictures
Nice to have
• inviting to join us on the guided dives
Should not have
• Any picture I didn't provide

```html
<!DOCTYPE html>
<html lang="en">
<head>
<meta charset="utf-8">
<title>Let us guide you – guided dives flyer</title>
<link rel="stylesheet" href="https://fonts.googleapis.com/css2?family=Poppins:ital,wght@0,400;0,500;0,600;0,700;0,800;1,500&display=swap">
<style>
  :root {
    --navy: #24306a;
    --navy-deep: #1d2759;
    --orange: #f0912c;
    --sky: #6fccea;
    --blue: #0677ba;
    --blue-bright: #0094d4;
    --paper: #f4f6f9;
    --white: #ffffff;
  }
  * { box-sizing: border-box; margin: 0; padding: 0; }
  html, body { width: 1200px; height: 1117px; overflow: hidden; }
  body {
    background: radial-gradient(ellipse at 70% 20%, #b9b9b9, #8f8f8f 80%);
    font-family: "Poppins", sans-serif;
  }
  .flyer {
    position: absolute; left: 230px; top: 36px;
    width: 740px; height: 1045px;
    background: var(--paper);
    overflow: hidden;
    box-shadow: 0 18px 40px rgba(0,0,0,.25);
  }
  .flyer-shapes { position: absolute; inset: 0; }

  .photo-circle {
    position: absolute; top: 270px; width: 124px; height: 124px; border-radius: 50%;
    border: 5px solid var(--white);
    box-shadow: 0 4px 12px rgba(0,0,0,.35);
  }
  .photo-circle--seahorse { left: 440px;
    background: radial-gradient(circle at 40% 45%, #c0704a, #2a6f86 55%, #0d3b52); }
  .photo-circle--food { left: 568px;
    background: radial-gradient(circle at 50% 50%, #e2a55a, #a8552e 55%, #5a3a2a); }

  .headline { position: absolute; left: 50px; top: 348px; line-height: .9; }
  .headline__lead { display: block; color: var(--white); font-weight: 800; font-size: 50px; letter-spacing: -2px; }
  .headline__main { display: block; font-weight: 800; font-size: 102px; letter-spacing: -3px; white-space: nowrap; }
  .headline__guide { color: var(--orange); }
  .headline__you { color: var(--sky); }

  .offer { position: absolute; left: 60px; top: 622px; width: 450px; }
  .offer__title { font-size: 28px; font-weight: 800; line-height: 1.08; color: var(--navy); }
  .offer__title em { font-style: normal; color: var(--orange); }
  .offer__list { list-style: none; margin-top: 18px; }
  .offer__item { position: relative; padding-left: 38px; font-size: 20px; font-weight: 500; color: var(--navy-deep); line-height: 1.2; margin-bottom: 10px; }
  .offer__item svg { position: absolute; left: 4px; top: 6px; }
  .offer__note { margin-top: 8px; font-size: 15px; font-style: italic; font-weight: 500; color: var(--navy); }

  .partners { position: absolute; right: 40px; top: 630px; width: 160px; display: flex; flex-direction: column; align-items: center; gap: 22px; }
  .brand { display: flex; align-items: center; gap: 8px; color: var(--navy); font-weight: 800; font-size: 19px; line-height: 1; }
  .brand__dot { width: 26px; height: 26px; border-radius: 50%; background: var(--orange); flex: none; }
  .partner-badge { width: 80px; height: 80px; border-radius: 50%; background: var(--blue-bright); }

  .contact-pill {
    position: absolute; height: 58px; border: 3px solid var(--orange); border-radius: 30px;
    display: flex; align-items: center; padding-left: 66px; color: var(--white);
  }
  .contact-pill__icon { position: absolute; left: -6px; top: -4px; width: 60px; height: 60px; border-radius: 50%; background: var(--orange); display: flex; align-items: center; justify-content: center; }
  .contact-pill__label { display: block; font-size: 11px; font-weight: 500; letter-spacing: .5px; color: var(--sky); text-transform: uppercase; }
  .contact-pill__value { display: block; font-size: 19px; font-weight: 600; line-height: 1.1; }
  .contact-pill--web { left: 48px; top: 868px; width: 320px; }
  .contact-pill--phone { left: 400px; top: 868px; width: 294px; }

  .contact-strip { position: absolute; top: 958px; height: 52px; display: flex; align-items: center; gap: 8px; color: var(--white); font-size: 18px; font-weight: 500; }
  .contact-strip--mail { left: 0; width: 290px; padding-left: 40px; background: var(--orange); clip-path: polygon(0 0,100% 0,92% 100%,0 100%); }
  .contact-strip--address { left: 266px; width: 474px; padding-left: 48px; background: var(--blue); clip-path: polygon(5% 0,100% 0,100% 100%,0 100%); }
</style>
</head>
<body>
<main class="flyer">
  <svg class="flyer-shapes" width="740" height="1045" viewBox="0 0 740 1045">
    <defs>
      <linearGradient id="coastTones" x1="0" y1="0" x2="1" y2="1">
        <stop offset="0" stop-color="#7fb3dc"/>
        <stop offset=".35" stop-color="#6b6a66"/>
        <stop offset=".6" stop-color="#2d8aa3"/>
        <stop offset="1" stop-color="#1c5f86"/>
      </linearGradient>
    </defs>
    <path class="header-band" d="M0 0H740V528C500 556 260 574 0 592Z" fill="var(--navy)"/>
    <path class="header-swoosh" d="M230 584C430 570 600 550 740 530" stroke="var(--orange)" stroke-width="12" fill="none"/>
    <path class="photo-frame" d="M172 0H740V352H330C240 352 172 284 172 196Z" fill="var(--sky)"/>
    <g role="img" aria-label="Photo of the rocky north coast of Bonaire with turquoise sea">
      <path d="M190 0H740V334H330C250 334 190 274 190 196Z" fill="url(#coastTones)"/>
    </g>
    <path class="contact-panel" d="M40 930C40 880 70 840 120 840H740V1045H0V930Z" fill="var(--navy)"/>
  </svg>

  <div class="photo-circle photo-circle--seahorse" role="img" aria-label="Photo of a seahorse on the reef"></div>
  <div class="photo-circle photo-circle--food" role="img" aria-label="Photo of authentic local lunch dishes"></div>

  <h1 class="headline">
    <span class="headline__lead">Let us</span>
    <span class="headline__main"><span class="headline__guide">guide</span> <span class="headline__you">you!</span></span>
  </h1>

  <section class="offer">
    <h2 class="offer__title"><em>2 guided dives</em> at the North side of Bonaire</h2>
    <ul class="offer__list">
      <li class="offer__item"><svg width="20" height="16" viewBox="0 0 20 16"><path d="M2 8l6 6L18 2" stroke="var(--sky)" stroke-width="4" fill="none"/></svg>We show you the cool stuff</li>
      <li class="offer__item"><svg width="20" height="16" viewBox="0 0 20 16"><path d="M2 8l6 6L18 2" stroke="var(--sky)" stroke-width="4" fill="none"/></svg>You just enjoy the dives, we take care of the rest</li>
    </ul>
    <p class="offer__note">Authentic local lunch and drinks at Posada Vista Alta</p>
  </section>

  <aside class="partners">
    <div class="brand"><span class="brand__dot"></span>Reef Trail Dive</div>
    <div class="partner-badge" aria-label="Certification partner"></div>
  </aside>

  <a class="contact-pill contact-pill--web">
    <span class="contact-pill__icon"><svg width="30" height="30" viewBox="0 0 30 30" fill="none" stroke="var(--navy)" stroke-width="2.4"><circle cx="15" cy="15" r="12"/><ellipse cx="15" cy="15" rx="5" ry="12"/><path d="M3 15h24M5 9h20M5 21h20"/></svg></span>
    <span><span class="contact-pill__label">Visit our website</span><span class="contact-pill__value">www.reeftraildive.com</span></span>
  </a>
  <a class="contact-pill contact-pill--phone">
    <span class="contact-pill__icon"><svg width="26" height="26" viewBox="0 0 24 24"><path d="M6.6 10.8a15 15 0 006.6 6.6l2.2-2.2a1 1 0 011-.25 11.4 11.4 0 003.6.6 1 1 0 011 1V20a1 1 0 01-1 1A17 17 0 013 4a1 1 0 011-1h3.5a1 1 0 011 1c0 1.25.2 2.45.6 3.6a1 1 0 01-.25 1z" fill="var(--navy)"/></svg></span>
    <span><span class="contact-pill__label">Call us</span><span class="contact-pill__value">+(599) 555 01 23</span></span>
  </a>

  <div class="contact-strip contact-strip--mail">
    <svg width="16" height="16" viewBox="0 0 16 16"><circle cx="8" cy="8" r="8" fill="var(--white)"/><rect x="4" y="5" width="8" height="6" fill="none" stroke="var(--orange)" stroke-width="1.3"/></svg>
    info@reeftraildive.com
  </div>
  <div class="contact-strip contact-strip--address">
    <svg width="14" height="18" viewBox="0 0 14 18"><path d="M7 0a7 7 0 017 7c0 5-7 11-7 11S0 12 0 7a7 7 0 017-7z" fill="var(--white)"/><circle cx="7" cy="7" r="2.5" fill="var(--blue)"/></svg>
    kaya marina 12, Kralendijk, Bonaire
  </div>
</main>
</body>
</html>
```